Brightfold Systems, a software development company, needs a website

We need a website to promote our software development company. The company is brand new and we want to market ourselves. We develop all kinds of software from web applications, to desktop applications, to mobile applications. Small company, not a lot of history, just need something flashy.

```html
<!DOCTYPE html>
<html lang="en">
<head>
<meta charset="utf-8">
<title>Brightfold Systems — Software Development</title>
<link href="https://fonts.googleapis.com/css2?family=Noto+Sans:wght@400;500;600;700&display=swap" rel="stylesheet">
<style>
:root{
  --red:#e3161d;
  --red-soft:#f0888b;
  --blush:#f8d3d4;
  --ink:#222226;
  --text:#444;
  --muted:#777;
  --night:#141418;
  --night-2:#0c0c10;
  --grey-bg:#efefef;
  --white:#fff;
}
*{box-sizing:border-box;margin:0;padding:0}
html,body{width:1200px;height:4360px;overflow:hidden}
body{position:relative;font-family:"Noto Sans",sans-serif;color:var(--text);background:var(--white)}
.abs{position:absolute}
a{color:inherit;text-decoration:none}

/* header */
.site-nav{position:absolute;left:0;top:0;width:1200px;height:74px;background:rgba(12,12,16,.82);z-index:5}
.brand{position:absolute;left:172px;top:20px;display:flex;align-items:center;gap:10px;color:var(--white);font-size:18px;font-weight:500}
.brand-dot{width:28px;height:28px;border-radius:50%;background:var(--red)}
.menu{position:absolute;left:448px;top:26px;display:flex;gap:30px;color:var(--white);font-size:13px}
.signup{position:absolute;left:935px;top:21px;height:28px;padding:0 34px 0 15px;border-radius:14px;background:var(--red);color:var(--white);font-size:13px;line-height:28px}
.signup i,.hero-btn i{position:absolute;right:4px;top:4px;width:20px;height:20px;border-radius:50%;background:var(--white)}
.signup i svg,.hero-btn i svg{display:block}

/* hero */
.hero{left:0;top:0;width:1200px;height:712px;background:linear-gradient(135deg,#3b3f45 0%,#5a5d62 40%,#2c2f33 75%,#45484c 100%)}
.hero-title{left:0;top:335px;width:1200px;text-align:center;color:var(--white);font-size:55px;font-weight:600}
.hero-btn{left:543px;top:432px;height:32px;width:112px;padding-left:14px;border-radius:16px;background:var(--red);color:var(--white);font-size:13px;line-height:32px}
.dots{left:570px;top:666px;display:flex;gap:8px}
.dots span{width:9px;height:9px;border-radius:50%;background:var(--white)}
.dots span.on{background:var(--red)}

h2.section-title{position:absolute;left:0;width:1200px;text-align:center;color:var(--ink);font-size:38px;font-weight:700}

/* applications */
.app-num{position:absolute;font-size:72px;font-weight:700;color:#e6e6e6;line-height:1}
.app-num::before{content:"";position:absolute;left:30px;top:0;width:50px;height:3px;background:var(--red)}
.app-title{position:absolute;font-size:24px;font-weight:600;color:var(--ink)}
.app-copy{position:absolute;width:406px;font-size:10.5px;line-height:20.3px;text-align:justify;color:var(--text)}
.more-btn{position:absolute;width:136px;height:42px;border:2px solid var(--red);border-radius:21px;color:var(--red);font-size:13px;font-weight:600;line-height:38px;padding-left:13px}
.more-btn i{position:absolute;right:4px;top:4px;width:30px;height:30px;border-radius:50%;background:var(--red)}
.more-btn i svg{display:block}
.photo{position:absolute;border-radius:16px;box-shadow:0 8px 22px rgba(0,0,0,.28)}

/* about */
.about-title{left:172px;top:2522px;color:var(--white);font-size:36px;font-weight:700;line-height:36px}
.about-copy{left:172px;top:2614px;width:332px;color:var(--white);font-size:10.5px;line-height:20.3px;text-align:justify}
.play{position:absolute;width:38px;height:38px;border-radius:50%;background:var(--red)}

/* why us */
.why-bg{left:0;top:2928px;width:1200px;height:381px;background:var(--grey-bg)}
.why-title{left:172px;top:3016px;color:var(--ink);font-size:35px;font-weight:700}
.why-copy{left:171px;top:3083px;width:258px;font-size:10px;line-height:20.3px;color:var(--text)}
.feature{position:absolute;width:270px;height:70px}
.feature h3{position:absolute;left:82px;top:2px;font-size:15px;font-weight:400;color:var(--ink)}
.feature p{position:absolute;left:84px;top:28px;width:180px;font-size:10px;line-height:16px;color:var(--muted)}
.feature svg{position:absolute;left:0;top:0}

/* blog */
.blog-lead{left:320px;top:3443px;width:560px;text-align:center;font-size:10.5px;line-height:20px;color:var(--text)}
.blog-card{position:absolute;top:3522px;width:414px;height:354px}
.blog-card h3{position:absolute;left:19px;top:272px;width:320px;color:var(--white);font-size:21px;font-weight:400;line-height:27px}
.blog-card .play{left:360px;top:284px;width:34px;height:34px}

/* footer */
.footer{left:0;top:3990px;width:1200px;height:370px;background:var(--night)}
.foot-col{position:absolute;top:4086px;color:var(--white)}
.foot-col h4{font-size:14px;font-weight:700;margin-bottom:14px}
.foot-col li{list-style:none;font-size:11px;line-height:22.5px;color:#ccc}
.contact-row{position:relative;padding-left:33px;font-size:11px;line-height:18px;color:#ccc;margin-bottom:16px}
.contact-row svg{position:absolute;left:0;top:2px}
.copyright{left:181px;top:4316px;font-size:10.5px;color:#ccc}
.socials{left:884px;top:4313px;display:flex;gap:16px}
.socials span{width:18px;height:18px;border-radius:50%;background:var(--white)}
.socials span:first-child{background:var(--red)}
</style>
</head>
<body>

<!-- Hero -->
<div class="abs hero" role="img" aria-label="Top-down photo of people working at a desk with laptops, keyboard and a potted plant, darkened"></div>
<header class="site-nav">
  <a class="brand" href="#"><span class="brand-dot"></span>Brightfold Systems</a>
  <nav class="menu"><a>Home</a><a>About Us</a><a>Applications</a><a>What We Do</a><a>News</a><a>Contact</a></nav>
  <a class="signup" href="#">Sign Up<i><svg width="20" height="20" viewBox="0 0 20 20"><path d="M5 10h9M11 7l3 3-3 3" stroke="#e3161d" stroke-width="1.6" fill="none"/></svg></i></a>
</header>
<h1 class="abs hero-title">Brightfold Systems</h1>
<a class="abs hero-btn" href="#">Read More<i><svg width="20" height="20" viewBox="0 0 20 20"><path d="M5 10h9M11 7l3 3-3 3" stroke="#e3161d" stroke-width="1.6" fill="none"/></svg></i></a>
<div class="abs dots"><span></span><span class="on"></span><span></span><span></span></div>
<svg class="abs" style="left:0;top:660px" width="1200" height="60" viewBox="0 0 1200 60" preserveAspectRatio="none">
  <path d="M0 40 C300 30 400 0 600 12 C800 25 950 20 1200 20 L1200 60 L0 60Z" fill="#fff"/>
  <path d="M0 36 C300 26 400 -4 600 8 C800 21 950 16 1200 14 L1200 22 C950 22 800 28 600 16 C400 4 300 34 0 44Z" fill="#e3161d"/>
</svg>

<h2 class="section-title" style="top:772px">Our Applications</h2>

<!-- Web -->
<svg class="abs" style="left:138px;top:897px" width="440" height="390" viewBox="0 0 440 390">
  <path d="M60 20 C140 -10 260 20 320 40 C360 55 330 120 360 150 C430 190 440 260 380 290 C300 330 250 390 150 370 C60 350 0 300 5 200 C8 120 10 40 60 20Z" fill="#f8d3d4"/>
  <path d="M350 150 C420 150 440 230 395 270 L360 280Z" fill="#f0888b"/>
</svg>
<div class="photo" style="left:227px;top:939px;width:291px;height:334px;background:linear-gradient(160deg,#6b6e72,#3e4145 55%,#8a7866)" role="img" aria-label="Laptop on a wooden desk next to a plant and a phone"></div>
<span class="app-num" style="left:586px;top:930px">01</span>
<h3 class="app-title" style="left:614px;top:940px">Web Applications</h3>
<p class="app-copy" style="left:617px;top:994px">At vero eos et accusamus et iusto odio dignissimos ducimus qui blanditiis praesentium voluptatum deleniti atque corrupti quos dolores et quas molestias excepturi sint occaecati cupiditate non provident, similique sunt in culpa qui officia deserunt mollitia animi, id est laborum et dolorum fuga. Et harum quidem rerum facilis est et expedita distinctio. Nam libero tempore, cum soluta nobis est eligendi optio cumqAt vero eos et accusamus et iusto odio dignissimos ducimus qui blanditiis praesentium voluptatum deleniti atque corrupti quos dolores et quas molestias excepturi sint occaecati cupiditate non providen</p>
<a class="more-btn" style="left:621px;top:1174px">Read More<i><svg width="30" height="30" viewBox="0 0 30 30"><path d="M8 15h13M17 11l4 4-4 4" stroke="#fff" stroke-width="2" fill="none"/></svg></i></a>

<!-- Desktop -->
<svg class="abs" style="left:700px;top:1305px" width="412" height="330" viewBox="0 0 412 330">
  <path d="M120 20 C200 -10 300 10 360 40 C420 80 410 180 390 250 C370 310 320 330 260 320 L180 300 C120 280 40 250 10 190 C-10 140 40 60 120 20Z" fill="#f8d3d4"/>
  <path d="M60 70 C20 120 0 180 20 220 L80 240Z" fill="#f0888b"/>
</svg>
<div class="photo" style="left:751px;top:1353px;width:293px;height:262px;background:linear-gradient(150deg,#f2f2f2,#c9cbcd 60%,#9a9ea2)" role="img" aria-label="Desktop computer on an office desk"></div>
<div class="photo" style="left:670px;top:1517px;width:252px;height:208px;background:linear-gradient(150deg,#4a4d52,#2a2c30 60%,#6a5c4e)" role="img" aria-label="Team working together around desktop computers"></div>
<span class="app-num" style="left:143px;top:1389px">02</span>
<h3 class="app-title" style="left:171px;top:1399px">Desktop Applications</h3>
<p class="app-copy" style="left:174px;top:1452px">At vero eos et accusamus et iusto odio dignissimos ducimus qui blanditiis praesentium voluptatum deleniti atque corrupti quos dolores et quas molestias excepturi sint occaecati cupiditate non provident, similique sunt in culpa qui officia deserunt mollitia animi, id est laborum et dolorum fuga. Et harum quidem rerum facilis est et expedita distinctio. Nam libero tempore, cum soluta nobis est eligendi optio cumqAt vero eos et accusamus et iusto odio dignissimos ducimus qui blanditiis praesentium voluptatum deleniti atque corrupti quos dolores et quas molestias excepturi sint occaecati cupiditate non providen</p>
<a class="more-btn" style="left:178px;top:1633px">Read More<i><svg width="30" height="30" viewBox="0 0 30 30"><path d="M8 15h13M17 11l4 4-4 4" stroke="#fff" stroke-width="2" fill="none"/></svg></i></a>

<!-- Mobile -->
<svg class="abs" style="left:139px;top:1836px" width="420" height="436" viewBox="0 0 420 436">
  <path d="M80 30 C160 0 260 40 330 90 C400 150 400 260 330 340 C270 410 180 440 100 410 C30 380 0 300 5 200 C10 120 20 60 80 30Z" fill="#f8d3d4"/>
</svg>
<div class="abs" style="left:154px;top:1840px;width:280px;height:280px;border-radius:50%;background:linear-gradient(135deg,#3a3a3e,#caa28a 50%,#2a2a2e)" role="img" aria-label="Hands holding a smartphone full of app icons"></div>
<div class="abs" style="left:398px;top:1873px;width:155px;height:155px;border-radius:50%;background:linear-gradient(135deg,#6a6e74,#2e3034)" role="img" aria-label="Phone in hand, blurred"></div>
<div class="abs" style="left:337px;top:1996px;width:226px;height:226px;border-radius:50%;border:4px solid #fff;background:linear-gradient(160deg,#cfe3f0,#3c7bb0 55%,#1b2530)" role="img" aria-label="Hand holding a phone with floating app screens"></div>
<span class="app-num" style="left:581px;top:1860px">03</span>
<h3 class="app-title" style="left:614px;top:1871px">Mobile Applications</h3>
<p class="app-copy" style="left:617px;top:1924px">At vero eos et accusamus et iusto odio dignissimos ducimus qui blanditiis praesentium voluptatum deleniti atque corrupti quos dolores et quas molestias excepturi sint occaecati cupiditate non provident, similique sunt in culpa qui officia deserunt mollitia animi, id est laborum et dolorum fuga. Et harum quidem rerum facilis est et expedita distinctio. Nam libero tempore, cum soluta nobis est eligendi optio cumqAt vero eos et accusamus et iusto odio dignissimos ducimus qui blanditiis praesentium voluptatum deleniti atque corrupti quos dolores et quas molestias excepturi sint occaecati cupiditate non providen</p>
<a class="more-btn" style="left:621px;top:2105px">Read More<i><svg width="30" height="30" viewBox="0 0 30 30"><path d="M8 15h13M17 11l4 4-4 4" stroke="#fff" stroke-width="2" fill="none"/></svg></i></a>

<!-- About band -->
<svg class="abs" style="left:0;top:2384px" width="1200" height="550" viewBox="0 0 1200 550" preserveAspectRatio="none" role="img" aria-label="Red band over a faint city skyline">
  <defs><linearGradient id="aboutRed" x1="0" y1="0" x2="0" y2="1"><stop offset="0" stop-color="#d8141b"/><stop offset="1" stop-color="#e51c22"/></linearGradient></defs>
  <path d="M0 30 C250 -10 400 40 650 20 C850 5 1000 -5 1200 10 L1200 520 C950 520 800 555 600 525 C400 495 250 505 0 490Z" fill="#bdbdbd"/>
  <path d="M0 42 C250 2 400 52 650 32 C850 17 1000 7 1200 22 L1200 505 C950 508 800 540 600 512 C400 484 250 490 0 478Z" fill="url(#aboutRed)"/>
</svg>
<h2 class="abs about-title">About Brightfold<br>Systems</h2>
<p class="abs about-copy">At vero eos et accusamus et iusto odio dignissimos ducimus qui blanditiis praesentium voluptatum deleniti atque corrupti quos dolores et quas molestias excepturi sint occaecati cupiditate non provident, similique sunt in culpa qui officia deserunt mollitia animi, id est laborum et dolorum fuga. Et harum quidem rerum facilis est et expedita distinctio. Nam libero tempore, cum soluta nobis est eligendi optio cumqAt vero eos et accusamus et iusto odio digni ssimos ducimus qui blanditiis</p>
<div class="photo" style="left:538px;top:2505px;width:567px;height:296px;background:linear-gradient(135deg,#e8e6e2,#8f8a86 45%,#4a4c50 80%)" role="img" aria-label="Team of developers gathered around computers in a bright office"></div>
<span class="play" style="left:574px;top:2731px"><svg width="38" height="38" viewBox="0 0 38 38"><path d="M16 13l9 6-9 6z" fill="#fff"/></svg></span>

<!-- Why us -->
<div class="abs why-bg"></div>
<h2 class="abs why-title">Why Us?</h2>
<p class="abs why-copy">At vero eos et accusamus et iusto odio dignissimos ducimus qui blanditiis praesentium voluptatum deleniti atrupti quos dolores et quas molestias excepturi sint occaecati cupiditate non provient, similique sunt blanditiis praesentium voluptatum deleniti atrupti quos dolores</p>
<svg class="abs" style="left:482px;top:3038px" width="560" height="186"><line x1="275" y1="0" x2="275" y2="186" stroke="#d4d4d4"/><line x1="0" y1="81" x2="560" y2="81" stroke="#d4d4d4"/></svg>
<div class="feature" style="left:490px;top:3036px">
  <svg width="66" height="66" viewBox="0 0 66 66" fill="none" stroke="#333" stroke-width="2"><rect x="3" y="6" width="40" height="30"/><path d="M10 28l9-10 8 6 10-12" stroke="#e3161d"/><circle cx="42" cy="42" r="11" stroke="#e3161d"/><path d="M50 50l12 12"/></svg>
  <h3>Consectetad</h3><p>Lorem ipsum dolloor sikit ameto nsectetadipcing el,bnp eiusm</p>
</div>
<div class="feature" style="left:786px;top:3036px">
  <svg width="66" height="66" viewBox="0 0 66 66" fill="none" stroke="#333" stroke-width="2"><circle cx="33" cy="18" r="10" stroke="#e3161d" stroke-dasharray="4 3"/><circle cx="33" cy="18" r="4" stroke="#e3161d"/><circle cx="14" cy="40" r="5"/><circle cx="33" cy="40" r="5"/><circle cx="52" cy="40" r="5"/><path d="M6 62v-10a8 8 0 0116 0v10M25 62v-10a8 8 0 0116 0v10M44 62v-10a8 8 0 0116 0v10"/></svg>
  <h3>Lorensectetad</h3><p>Lorem ipsum dolloor sikit ameto nsectetadipcing el,bnp eiusm</p>
</div>
<div class="feature" style="left:490px;top:3141px">
  <svg width="66" height="66" viewBox="0 0 66 66" fill="none" stroke="#333" stroke-width="2"><circle cx="10" cy="6" r="3" fill="#e3161d" stroke="none"/><circle cx="24" cy="4" r="3" fill="#e3161d" stroke="none"/><circle cx="38" cy="8" r="3" fill="#e3161d" stroke="none"/><path d="M4 16h40L30 34v12H18V34z"/><circle cx="24" cy="56" r="8" stroke="#e3161d"/><path d="M24 51v10" stroke="#e3161d"/></svg>
  <h3>Moreonsectetad</h3><p>Lorem ipsum dolloor sikit ameto nsectetadipcing el,bnp eiusm</p>
</div>
<div class="feature" style="left:786px;top:3141px">
  <svg width="66" height="66" viewBox="0 0 66 66" fill="none" stroke="#333" stroke-width="2"><rect x="2" y="4" width="56" height="54" rx="6"/><circle cx="30" cy="30" r="14" stroke="#e3161d"/><circle cx="30" cy="30" r="6" stroke="#e3161d"/><path d="M30 30l18 18M44 48h6v-6"/></svg>
  <h3>Sed onsectetad</h3><p>Lorem ipsum dolloor sikit ameto nsectetadipcing el,bnp eiusm</p>
</div>

<!-- Blog -->
<h2 class="section-title" style="top:3380px">Latest Blog</h2>
<p class="abs blog-lead">At vero eos et accusamus et iusto odio dignissimos ducimus qui blanditiis praesentium voluptatum deleniti at rupti quos dolores et quas molestias excepturi sint occaecati cupiditate non provident, similique sunt.</p>
<article class="blog-card" style="left:171px;background:linear-gradient(180deg,#d7d9da 0%,#8d9193 45%,#1d1e20 90%)" role="img" aria-label="People working at desks in an open-plan office">
  <h3>At vero eos et accusamut iusto odio dignissimos ducimu</h3>
  <span class="play"><svg width="34" height="34" viewBox="0 0 34 34"><path d="M14 11l9 6-9 6z" fill="#fff"/></svg></span>
</article>
<article class="blog-card" style="left:613px;background:linear-gradient(180deg,#2f4448 0%,#233033 45%,#111214 90%)" role="img" aria-label="Two developers looking at code on a monitor">
  <h3>At vero eos et accusamut iusto odio dignissimos ducimu</h3>
  <span class="play"><svg width="34" height="34" viewBox="0 0 34 34"><path d="M14 11l9 6-9 6z" fill="#fff"/></svg></span>
</article>

<!-- Footer -->
<svg class="abs" style="left:0;top:3950px" width="1200" height="60" viewBox="0 0 1200 60" preserveAspectRatio="none">
  <path d="M0 12 C200 40 400 40 600 22 C800 4 1000 10 1200 28 L1200 60 L0 60Z" fill="#e3161d"/>
  <path d="M0 22 C200 50 400 50 600 32 C800 14 1000 20 1200 38 L1200 60 L0 60Z" fill="#141418"/>
</svg>
<footer class="abs footer"></footer>
<div class="foot-col" style="left:181px">
  <h4>Contact</h4>
  <div class="contact-row"><svg width="18" height="20" viewBox="0 0 18 20" fill="none" stroke="#e3161d" stroke-width="1.5"><path d="M9 19s-7-7-7-11a7 7 0 0114 0c0 4-7 11-7 11z"/><circle cx="9" cy="8" r="2.5"/></svg>214 Larkspur Lane,<br>Eastmoor Quarter</div>
  <div class="contact-row"><svg width="18" height="20" viewBox="0 0 18 20" fill="none" stroke="#e3161d" stroke-width="1.5"><path d="M3 2h4l2 5-3 2a11 11 0 005 5l2-3 5 2v4a2 2 0 01-2 2C8 19 1 12 1 4a2 2 0 012-2z"/></svg>0 100 555 014 27<br>0 100 555 098 63</div>
  <div class="contact-row"><svg width="20" height="18" viewBox="0 0 20 18" fill="none" stroke="#e3161d" stroke-width="1.5"><rect x="1" y="3" width="18" height="12"/><path d="M1 3l9 7 9-7"/></svg>hello@brightfold.test<br>team@brightfold.test</div>
</div>
<div class="foot-col" style="left:447px"><h4>About Us</h4><ul><li>Lorem ipsum dolo</li><li>Consectetur adipiscing elit.</li><li>Fusce eget leo tincid</li><li>Donec consequat</li><li>Praesent elementum</li><li>Jmauris posueret</li></ul></div>
<div class="foot-col" style="left:677px"><h4>Information</h4><ul><li>Lorem ipsum dolo</li><li>Consectetur adipiscing elit.</li><li>Fusce eec consequat</li><li>Praesent elementum</li><li>Jmauris posueret</li><li>Aenean a ex eu lectu</li></ul></div>
<div class="foot-col" style="left:890px"><h4>Other Links</h4><ul><li>Lorem ipsum dolo</li><li>Consecteturiscing elit.</li><li>Fusce eget leo tincid</li><li>Donec consequat</li><li>Praesent elementum</li><li>Aenean a ex eu lectu</li></ul></div>
<p class="abs copyright">Copyright 2019 Brightfold Systems.All Rights Reserved</p>
<div class="abs socials" aria-label="Social links"><span></span><span></span><span></span><span></span><span></span></div>

</body>
</html>
```